Bright Path Safety billboard design project.

Bright Path Safety Ltd. is based in Quesnel BC and provides a variety of safety services including COR external auditing, safety training, over 500 online safety courses, mobile equipment training and heavy duty equipment training. We are looking for a billboard design with more of a focus on the mobile equipment training.

Target Market(s)

Construction, forestry and mining companies.

Colors
3276b5

Requirements
Must have
• Company Logo
website www.brightpathsafety-example.com

```html
<!DOCTYPE html>
<html lang="en">
<head>
<meta charset="utf-8">
<title>Bright Path Safety – Mobile Equipment Training Billboard</title>
<link rel="stylesheet" href="https://fonts.googleapis.com/css2?family=Poppins:wght@600;700&display=swap">
<style>
  :root {
    --page-bg: #e8e8e8;
    --brand-blue: #1b9ad6;
    --ink-dark: #3c3e43;
    --bar-grey: #4a4c51;
    --white: #ffffff;
    --photo-light: #eef1f4;
    --photo-mid: #cdd2d9;
    --photo-warm: #c9a98f;
  }
  html, body {
    margin: 0;
    padding: 0;
    width: 842px;
    height: 1200px;
    overflow: hidden;
    background: var(--page-bg);
  }
  .billboard {
    position: absolute;
    left: 21px;
    top: 425px;
    width: 800px;
    height: 349px;
    background: var(--white);
    box-shadow: 6px 8px 14px rgba(0,0,0,0.28);
    overflow: hidden;
  }
  .billboard svg { display: block; }
  .photo-area {
    position: absolute;
    left: 346px;
    top: 0;
    width: 454px;
    height: 308px;
    background:
      radial-gradient(ellipse at 70% 80%, rgba(226,120,40,0.45) 0%, rgba(226,120,40,0) 55%),
      linear-gradient(100deg, var(--white) 0%, var(--photo-light) 18%, var(--photo-mid) 60%, var(--photo-warm) 100%);
  }
  .art { position: absolute; left: 0; top: 0; }
  .headline { font-family: "Poppins", sans-serif; font-weight: 700; }
  .band-text { font-family: "Poppins", sans-serif; font-weight: 700; fill: var(--white); }
  .sub-text { font-family: "Poppins", sans-serif; font-weight: 700; }
  .phone-number { font-family: "Poppins", sans-serif; font-weight: 700; fill: var(--white); }
  .address { font-family: "Poppins", sans-serif; font-weight: 600; fill: var(--white); }
  .brand-name { font-family: "Poppins", sans-serif; font-weight: 700; fill: var(--ink-dark); }
</style>
</head>
<body>
  <div class="billboard">
    <div class="photo-area" role="img" aria-label="Photo of a worker driving an orange forklift carrying a pallet of bagged material inside a bright warehouse"></div>
    <svg class="art" width="800" height="349" viewBox="0 0 800 349">
      <!-- headline -->
      <text class="headline" x="25" y="62" font-size="44" fill="var(--brand-blue)" textLength="171" lengthAdjust="spacingAndGlyphs">MOBILE</text>
      <text class="headline" x="77" y="104" font-size="44" fill="var(--ink-dark)" textLength="269" lengthAdjust="spacingAndGlyphs">EQUIPMENT</text>
      <text class="headline" x="25" y="148" font-size="44" fill="var(--ink-dark)" textLength="228" lengthAdjust="spacingAndGlyphs">TRAINING</text>

      <!-- brand mark -->
      <circle cx="424" cy="80" r="64" fill="var(--white)" stroke="var(--brand-blue)" stroke-width="4"/>
      <text class="brand-name" x="424" y="76" font-size="15" text-anchor="middle">BRIGHT PATH</text>
      <text class="brand-name" x="424" y="95" font-size="15" text-anchor="middle">SAFETY LTD.</text>

      <!-- course band -->
      <rect x="0" y="164" width="355" height="59" fill="var(--brand-blue)"/>
      <text class="band-text" x="187" y="192" font-size="23" text-anchor="middle" textLength="120" lengthAdjust="spacingAndGlyphs">OVER 500</text>
      <text class="band-text" x="187" y="216" font-size="23" text-anchor="middle" textLength="307" lengthAdjust="spacingAndGlyphs">ONLINE SAFETY COURSES</text>

      <!-- secondary service -->
      <text class="sub-text" x="187" y="249" font-size="16" fill="var(--ink-dark)" text-anchor="middle" textLength="103" lengthAdjust="spacingAndGlyphs">WE ALSO DO</text>
      <text class="sub-text" x="187" y="268" font-size="16" fill="var(--brand-blue)" text-anchor="middle" textLength="291" lengthAdjust="spacingAndGlyphs">HEAVY DUTY EQUIPMENT TRAINING</text>

      <!-- address bar -->
      <polygon points="346,308 800,308 800,349 364,349" fill="var(--brand-blue)"/>
      <text class="address" x="380" y="335" font-size="17" textLength="401" lengthAdjust="spacingAndGlyphs">742 Alder Way, Quesnel, BC V2J 0A0, Canada</text>

      <!-- phone bar -->
      <polygon points="0,294 346,294 364,349 0,349" fill="var(--bar-grey)"/>
      <circle cx="34" cy="322" r="15" fill="var(--brand-blue)"/>
      <path d="M28.5 314.5c1-.9 2.3-.7 2.9.3l1.7 2.8c.5.9.3 2-.5 2.6l-1.2.9c.9 2 2.6 3.8 4.6 4.8l.9-1.2c.6-.8 1.7-1 2.6-.5l2.8 1.7c1 .6 1.2 1.9.3 2.9l-1.3 1.4c-1.2 1.3-3.1 1.6-4.7.8-4.6-2.3-8.2-5.9-10.4-10.4-.8-1.6-.5-3.5.8-4.7z" fill="var(--white)"/>
      <text class="phone-number" x="61" y="335" font-size="36" textLength="266" lengthAdjust="spacingAndGlyphs">250-555-0147</text>
    </svg>
  </div>
</body>
</html>
```